Packaging Design Project For Chocolate Brand

We need a fresh, vibrant and colourful packaging for our healthy chocolate brand, oPickFernwobble.

WHAT IS oPickFernwobble?

oPickFernwobble are indulgent chocolates that help reduce your body weight by controlling your appetite and calorie intake. And the best thing is that it tastes 100% genuine chocolate, only healthier.

WHAT WE NEED FROM YOU

Although we have collected a few logos from other designers, it's not quite catchy to the eye. As it will appear on retail shelves, it needs to catch the eye. It's up to the designers if they want to design the logo all in one word or two words. We will provide feedback quickly. We are contemplating on a sub-title beneath the logo, with the words "Unwrap. Eat. Lose." It is the main logo "oPickFernwobble" that needs to stand out though with possibly some chocolatey or slimming/dieting aspect. However we do not want any images of thin bodies around the logo. Use of imagination involving chocolate could be beneficial, e.g. melting chocolate etc.
Use different colours for 'i', 'Love', and 'Fernwobble'. Maybe include an illustration around the logo if you feel it will brighten the brand.

Packaging

Although we do not have a specific theme in mind, the designer may want to try a retro look with illustrations/images, funky, maybe professional but keep it modern and looking like a chocolate bar.

Dimensions - 155mm(width) x 76.8mm(height) x 34mm(depth)
Portrait or landscape. Designers choice.

There are three flavours, Milk, White and Dark so three different packages with different colours. The rest of the packages will look more or less the same. The packaging itself needs 'wavey' aspects of chocolate. Wavey, circular, elegant shapes which appeal to the eye

There are certain texts which need to go on the front end of the box. The designer has the option of using 2 different texts in their work to come up with the best design. Texts are on the files. More text may be added but in the meantime please use what is given.

Project Deadline Extended
Reason: Hi, The deadline has been extended a further 7 days for those who designers who started their designs late are concerned about the timeframe. So there is no need to rush your designs. I hope the 7 days extension is enough for those that need it. Many thanks,

Target Market(s)

Women aged 16-45, C1C2 class

Industry/Entity Type

Landscape

Requirements
Must have
• Appealing mostly to women aged 16-45, C1C2 class.
Colourful
Chocolatey feel with wavey lines etc
Strong Logo
Nice to have
• It can come across as a food supplement that you normally see on the pharmacy shelf but with an unconventional design twist. Or the designer may think it will not work and for it to have the chocolatey feel, there cannot be any connection a pharmaceutical package. It has to remain like a regular chocolate bar that you see in the supermarket. Up to the designer to choose. It will be going into both supermarket stores and healthfood stores.

The designer should have some personal input in the design. If you were browsing around the supermarket and spotted it, would you stop and look at it? If not, the design will need changing.

Secondly, maybe a brand illustration would go well with the logo. Possibly an animal illustration relating to chocolate (somehow) or simply a chocolate with a measuring tape around it getting slimmer and slimmer. Just a few thoughts

```html
<!DOCTYPE html>
<html lang="en">
<head>
<meta charset="utf-8">
<title>oPickFernwobble Dark Chocolate Pack Front</title>
<link rel="stylesheet" href="https://fonts.googleapis.com/css2?family=Cinzel:wght@700&family=Cormorant+Garamond:ital,wght@1,600&family=Quicksand:wght@500&display=swap">
<style>
  :root {
    --page: #ffffff;
    --pack-orange: #ef9d18;
    --pack-amber: #f4b21c;
    --pack-yellow: #f9cb22;
    --pack-glow: #fde27a;
    --emboss: rgba(160, 80, 10, 0.35);
    --quote: #7a2610;
    --brand: #4a1c0e;
    --ribbon: #4a1a0c;
    --ribbon-text: #f6dcae;
    --badge-dark: #2b0f07;
    --badge-gold: #d8a53a;
    --badge-gold-light: #f5d98a;
    --label-black: #120603;
    --label-white: #ffffff;
    --choc-deep: #3a1608;
    --choc-mid: #6b3418;
    --pattern-tone: rgba(225, 140, 20, 0.45);
  }
  html, body {
    margin: 0;
    width: 890px;
    height: 1200px;
    overflow: hidden;
    background: var(--page);
  }
  .canvas {
    position: relative;
    width: 890px;
    height: 1200px;
  }
  .pack-front {
    position: absolute;
    left: 215px;
    top: 95px;
    width: 470px;
    height: 1005px;
    overflow: hidden;
    background: linear-gradient(180deg, var(--pack-orange) 0%, var(--pack-amber) 30%, var(--pack-yellow) 50%, var(--pack-amber) 75%, var(--pack-orange) 100%);
  }
  .paisley-upper {
    position: absolute;
    left: 0; top: 180px;
    width: 470px; height: 260px;
    background: radial-gradient(ellipse at 50% 50%, var(--pattern-tone) 0%, rgba(225,140,20,0) 70%);
  }
  .fold-glow {
    position: absolute;
    left: 0; top: 440px;
    width: 470px; height: 300px;
    background: radial-gradient(ellipse at 50% 10%, var(--pack-glow) 0%, rgba(253,226,122,0) 70%);
  }
  .paisley-lower {
    position: absolute;
    left: 0; bottom: 0;
    width: 470px; height: 150px;
    background: linear-gradient(180deg, rgba(225,140,20,0) 0%, var(--pattern-tone) 100%);
  }
  .category {
    position: absolute;
    top: 48px; left: 0; width: 470px;
    margin: 0;
    text-align: center;
    font-family: "Cinzel", serif;
    font-size: 22px;
    letter-spacing: 1px;
    color: var(--emboss);
  }
  .tagline {
    position: absolute;
    top: 88px; left: 0; width: 470px;
    margin: 0;
    text-align: center;
    font-family: "Cormorant Garamond", serif;
    font-style: italic;
    font-weight: 600;
    font-size: 30px;
    line-height: 46px;
    color: var(--quote);
  }
  .brand-dot {
    position: absolute;
    left: 215px; top: 500px;
    width: 40px; height: 40px;
    border-radius: 50%;
    background: var(--badge-gold);
  }
  .brand-name {
    position: absolute;
    top: 560px; left: 0; width: 470px;
    margin: 0;
    text-align: center;
    font-family: "Quicksand", sans-serif;
    font-weight: 500;
    font-size: 50px;
    color: var(--brand);
  }
  .slogan-ribbon {
    position: absolute;
    left: 85px; top: 640px;
    width: 300px; height: 54px;
  }
  .slogan-text {
    position: absolute;
    left: 85px; top: 647px;
    width: 300px;
    margin: 0;
    text-align: center;
    font-family: "Cormorant Garamond", serif;
    font-style: italic;
    font-weight: 600;
    font-size: 24px;
    color: var(--ribbon-text);
  }
  .flavour-badge {
    position: absolute;
    left: 90px; top: 700px;
    width: 290px; height: 270px;
  }
  .flavour-label {
    position: absolute;
    left: 100px; top: 772px;
    width: 270px;
    text-align: center;
  }
  .flavour-name {
    margin: 0;
    font-family: "Cinzel", serif;
    font-weight: 700;
    font-size: 20px;
    color: var(--label-white);
    line-height: 24px;
  }
  .flavour-count {
    margin: 0;
    font-family: "Cinzel", serif;
    font-weight: 700;
    font-size: 11px;
    color: var(--badge-gold-light);
  }
  .chocolate-swirl {
    position: absolute;
    left: 120px; top: 835px;
    width: 230px; height: 115px;
    border-radius: 0 0 115px 115px;
    background: radial-gradient(ellipse at 50% 35%, var(--choc-mid) 0%, var(--choc-deep) 75%);
  }
</style>
</head>
<body>
<main class="canvas">
  <section class="pack-front">
    <div class="paisley-upper" role="img" aria-label="Faint golden paisley and floral pattern"></div>
    <div class="fold-glow"></div>
    <div class="paisley-lower" role="img" aria-label="Golden paisley ornaments along the bottom edge"></div>

    <p class="category">HEALTHY CHOCOLATE</p>
    <p class="tagline">"Open Me and Say...<br>...Hello Skinny Jeans"</p>

    <span class="brand-dot"></span>
    <h1 class="brand-name">oPickFernwobble</h1>

    <svg class="slogan-ribbon" viewBox="0 0 300 54" aria-hidden="true">
      <polygon points="0,14 24,14 24,50 0,50 10,32" fill="var(--ribbon)" opacity="0.8"/>
      <polygon points="300,14 276,14 276,50 300,50 290,32" fill="var(--ribbon)" opacity="0.8"/>
      <path d="M18,4 Q150,14 282,4 L282,40 Q150,50 18,40 Z" fill="var(--ribbon)"/>
    </svg>
    <p class="slogan-text">Unwrap, Eat, Lose</p>

    <svg class="flavour-badge" viewBox="0 0 290 270" aria-hidden="true">
      <path d="M40,20 L110,20 Q145,0 180,20 L250,20 L280,70 L280,190 Q280,265 145,265 Q10,265 10,190 L10,70 Z"
            fill="var(--badge-dark)" stroke="var(--badge-gold)" stroke-width="6"/>
      <line x1="50" y1="50" x2="240" y2="50" stroke="var(--badge-gold)" stroke-width="2"/>
      <line x1="60" y1="60" x2="230" y2="60" stroke="var(--badge-gold)" stroke-width="1.5"/>
      <rect x="5" y="66" width="280" height="58" rx="10" fill="var(--label-black)" stroke="var(--badge-gold)" stroke-width="3"/>
    </svg>
    <div class="flavour-label">
      <p class="flavour-name">DARK CHOCOLATE</p>
      <p class="flavour-count">12 x 15.5g Chocolate Minibars</p>
    </div>
    <div class="chocolate-swirl" role="img" aria-label="Melted dark chocolate with a falling drop and ripples"></div>
  </section>
</main>
</body>
</html>
```